Bright Acorn day Nursery flyer

I need a great flyer to attract new parents. Bright Acorn Is a fantastic, warm and homely nursery in Westmere road SE6 London. We offer many things that other nurseries don't offer such as Spanish, Yoga, Music, Cooking classes and Makaton. We also have an amazing system called KINDTRAK that allows parents to get alerts on the KINDTRAK app about their children daily activities and even developmental reports. Parents are able to share with the nursery great moments and put pictures and videos through the app. We also offer the parent camera, an extremely safe system that allows parents to log in and see their children whilst they are engaged in exciting activities.
Full details of Nursery
87 Westmere road
SE6 4QP
02084417260
www.brightacornhollis.co.uk
facebook page
brightacorndaynursery@brightacornhollis.co.uk
Updates

double sided or mini brochure type

Hi Please keep it simple and clean I feel the designs are a good attempt thank you but they are very busy and I just want to add important points a lot of the designs have too many colours, too much text etc Thank you!

https://www.facebook.com/brightacornhollis.co.uk/

Target Market(s)

parents of children 0-5

Industry/Entity Type

Childcare

Colors

Designer to choose colors to be used in the design.

Requirements
Must have
• colour and pictures but clean design

```html
<!DOCTYPE html>
<html lang="en">
<head>
<meta charset="utf-8">
<title>Bright Acorn Day Nursery – Flyer</title>
<link href="https://fonts.googleapis.com/css2?family=Roboto+Condensed:wght@700&family=Lato:wght@400;700&family=Montserrat:wght@500;700&family=Anton&family=Open+Sans&display=swap" rel="stylesheet">
<style>
:root{
  --stage:#4a4848;
  --blue:#3452a4;
  --green-light:#d6f02a;
  --green-deep:#4cc138;
  --mint:#6cc980;
  --orange:#f6b21b;
  --teal:#1aa89a;
  --lime:#d2e812;
  --purple:#9b2f9a;
  --magenta:#c81e70;
  --ink:#1a1a1a;
}
*{margin:0;padding:0;box-sizing:border-box}
html,body{width:1200px;height:1200px;overflow:hidden;background:var(--stage)}
.stage{position:relative;width:1200px;height:1200px}
.sheet{position:absolute;overflow:hidden;box-shadow:3px 4px 8px rgba(0,0,0,.45)}
.sheet-label{position:absolute;top:966px;font:400 44px/1 "Open Sans",sans-serif;color:#fff;transform:translateX(-50%)}

/* Front */
.front{left:70px;top:214px;width:520px;height:730px;
  background:radial-gradient(circle at 50% 10%,#3a5cb2 0%,var(--blue) 70%)}
.front .wave{position:absolute;left:0;top:0}
.front .headline{position:absolute;left:0;width:100%;text-align:center;font-family:"Roboto Condensed",sans-serif;font-weight:700;line-height:1}
.welcome{top:40px;font-size:60px;color:var(--mint)}
.name{top:100px;font-size:48px;color:var(--orange)}
.nursery{top:148px;font-size:60px;color:var(--mint)}
.intro{position:absolute;left:30px;right:30px;top:230px;text-align:center;font:700 13.2px/1.26 "Lato",sans-serif;color:#fff}
.intro-small{position:absolute;left:25px;right:32px;top:292px;font:400 9.6px/1.45 "Lato",sans-serif;color:#e8ecf8;text-align:justify}
.intro-small b{font-weight:700;color:#fff}
.url{position:absolute;left:0;width:510px;top:341px;text-align:center;font:700 15px/1 "Roboto Condensed",sans-serif;color:#fff}
.logo-badge{position:absolute;left:359px;top:330px;width:140px;height:140px;border-radius:50%;background:#fff;border:5px solid var(--teal);display:flex;flex-direction:column;align-items:center;justify-content:center;gap:6px}
.logo-badge .dot{width:26px;height:26px;border-radius:50%;background:var(--orange)}
.logo-badge .brand{font:700 15px/1 "Lato",sans-serif;color:var(--teal)}
.photo{position:absolute;border-radius:50%}
.photo-main{left:146px;top:446px;width:208px;height:208px;border:5px solid var(--teal);background:radial-gradient(circle at 50% 40%,#f3d8c6,#b89a80)}
.photo-paint{left:102px;top:416px;width:112px;height:112px;border:4px solid #e32b2b;background:radial-gradient(circle,#f0e0d6,#c9a48d)}
.photo-play{left:302px;top:576px;width:88px;height:88px;border:4px solid var(--purple);background:radial-gradient(circle,#e7c7c2,#a7867f)}
.contact{position:absolute;left:0;width:100%;top:690px;display:flex;justify-content:center;align-items:center;gap:22px;font:700 13.6px/1 "Roboto Condensed",sans-serif;color:var(--ink)}
.contact .rule{width:2px;height:17px;background:var(--ink)}

/* Back */
.back{left:626px;top:216px;width:515px;height:724px;
  background:radial-gradient(circle at 70% 60%,#e7f21e 0%,var(--lime) 60%,#c8e10e 100%)}
.back h2{position:absolute;left:38px;top:28px;font:700 52px/1 "Roboto Condensed",sans-serif;color:var(--purple)}
.copy{position:absolute;left:26px;width:462px;font:500 9.7px/1.27 "Montserrat",sans-serif;color:var(--ink);text-align:justify}
.p1{top:96px}.p2{top:157px}.p3{top:206px}
.bar{position:absolute;left:34px;width:454px;height:24px;background:var(--purple);font:700 14px/24px "Montserrat",sans-serif;color:var(--orange);padding-left:30px}
.bar-hours{top:312px}.bar-curr{top:396px}
.bar-icon{position:absolute;left:-8px;top:-6px;width:34px;height:34px;border-radius:50%;background:var(--lime);border:3px solid var(--purple)}
.list{position:absolute;left:33px;list-style:none;font:500 11.2px/1 "Montserrat",sans-serif;color:var(--ink)}
.list li{position:relative;padding-left:18px;height:20px;display:flex;align-items:center}
.list li::before{content:"";position:absolute;left:0;top:4px;border-left:13px solid var(--purple);border-top:6px solid transparent;border-bottom:6px solid transparent}
.list em{font-style:normal;color:var(--purple)}
.hours{top:343px}
.hours li{height:20px}
.curriculum{top:429px}
.dot-deco{position:absolute;border-radius:50%}
.d1{left:330px;top:512px;width:48px;height:48px;background:var(--magenta)}
.d2{left:450px;top:652px;width:36px;height:36px;background:var(--purple)}
.d3{left:474px;top:648px;width:16px;height:16px;background:#e3263a}
.photo-back{left:329px;top:528px;width:132px;height:132px;border:5px solid var(--purple);background:radial-gradient(circle,#f2e6dc,#c7aa94)}
.we-offer{position:absolute;left:30px;top:586px;font:400 58px/1 "Anton",sans-serif;color:var(--magenta);-webkit-text-stroke:2px #fff;paint-order:stroke fill;letter-spacing:1px}
.offers{position:absolute;left:27px;top:674px;display:flex;gap:6px;font:700 19px/1 "Montserrat",sans-serif;color:var(--magenta)}
.offers .sep{width:2px;height:22px;background:var(--magenta)}
</style>
</head>
<body>
<div class="stage">

  <section class="sheet front" aria-label="Flyer front">
    <svg class="wave" width="520" height="730" viewBox="0 0 520 730" aria-hidden="true">
      <defs>
        <radialGradient id="frontGreen" cx="45%" cy="35%" r="80%">
          <stop offset="0" stop-color="#dbf22c"/>
          <stop offset="1" stop-color="#4cc138"/>
        </radialGradient>
      </defs>
      <path d="M0 426 Q220 370 400 384 Q480 392 520 420 L520 730 L0 730 Z" fill="url(#frontGreen)" stroke="#1aa89a" stroke-width="5"/>
    </svg>
    <div class="headline welcome">Welcome to</div>
    <div class="headline name">Bright Acorn Day</div>
    <div class="headline nursery">Nursery</div>
    <p class="intro">We also have an amazing system called KINDTRAK that allows parents to get alerts on the KINDTRAK app about their children daily activities and even developmental reports.</p>
    <p class="intro-small"><b>Parents are able to share with the nursery great moments and put pictures and videos through the app.</b> We also offer the parent camera, an extremely safe system that allows parents to log in and see their children whilst they are engaged in exciting activities.</p>
    <div class="url">www.brightacornhollis.co.uk</div>
    <div class="logo-badge"><span class="dot"></span><span class="brand">Bright Acorn</span></div>
    <div class="photo photo-paint" role="img" aria-label="Photo of a young girl with paint on her hands and face"></div>
    <div class="photo photo-main" role="img" aria-label="Portrait photo of a smiling young girl"></div>
    <div class="photo photo-play" role="img" aria-label="Photo of a toddler playing outdoors"></div>
    <div class="contact"><span>Call us 02084417260 for know more detais</span><span class="rule"></span><span>87 Westmere road SE6 4QP</span></div>
  </section>

  <section class="sheet back" aria-label="Flyer back">
    <h2>Learning through play</h2>
    <p class="copy p1">We are a privately owned, vibrant nursery offering your child a caring, family environment within the popular Hollis Estate. We offer high quality day care for all children from 3 months to 5 years, treating each child as a treasured individual.</p>
    <p class="copy p2">At Bright Acorn we know that choosing the best nursery for your child is vital but it can seem very daunting. You need to be absolutely sure you have made the right decision to give you peace of mind.</p>
    <p class="copy p3">We have established this nursery very much from a parents' perspective. We have a passion for delivering high quality care, love and fun learning opportunities. This is at the heart of Bright Acorn. We provide a loving and nurturing family environment enabling children to experience such homely activities as they would at home both within the setting and also in the local community. We promote confident, happy, caring, collaborative learners. We also aspire for the children and our staff to achieve highly as they develop and grow in all aspects.</p>

    <div class="bar bar-hours"><span class="bar-icon"></span>Hours</div>
    <ul class="list hours">
      <li>Nursery opening hours are&nbsp;<em>7.45am to 6:15pm.</em></li>
      <li>A session can be either&nbsp;<em>7.45am to 12.45pm</em>&nbsp;or&nbsp;<em>1.15pm to 6:15pm</em>.</li>
    </ul>

    <div class="bar bar-curr"><span class="bar-icon"></span>Our Cariculam</div>
    <ul class="list curriculum">
      <li>Communication and Language</li>
      <li>Physical Development</li>
      <li>Personal, Social and Emotional Development</li>
      <li>Literacy</li>
      <li>Mathematics</li>
      <li>Understanding the World</li>
      <li>Expressive Arts and Desig</li>
    </ul>

    <span class="dot-deco d1"></span>
    <div class="photo photo-back" role="img" aria-label="Photo of a toddler with painted hands and face"></div>
    <span class="dot-deco d2"></span>
    <span class="dot-deco d3"></span>

    <div class="we-offer">WE OFFER</div>
    <div class="offers"><span>Spanish</span><span class="sep"></span><span>Yoga</span><span class="sep"></span><span>Music</span><span class="sep"></span><span>Cooking</span><span class="sep"></span><span>Makaton</span></div>
  </section>

  <div class="sheet-label" style="left:312px">Front</div>
  <div class="sheet-label" style="left:870px">Back</div>
</div>
</body>
</html>
```